Vero M.Q. - Diagnostic Ultrasound Flyer

About US
Vero M.Q. is a concierge ultrasound company that provides onsite or offsite diagnostic ultrasounds. We have over 14 years experience in sonography, business management, and customer service. We offer both the physician and patient flexibility, convenience, and access to timely services.

We provide ultrasounds for the following specialties:
Obstetrics/Gynecology
Abdominal
Small Parts
Vascular

Company Features:
1. Onsite or Offsite Scans
2. Images Available Immediately for Referring Physician and Patient
3. Flexible Options for Ultrasound Interpretation/Billing
4. Access to Interpreting Radiologist
5. Final Report Process - 1-2 Business Days/ 1 hour for STAT.
6. PACS Storage with Secure Access.

We need a place to add in our contact information (address, email, website, phone)

We already have a logo and would like to use it ( they are attached). We would the colors to match the logo colors....maybe lighter version of yellow and blue.

```html
<!DOCTYPE html>
<html lang="en">
<head>
<meta charset="utf-8">
<title>Vero M.Q. – Diagnostic Ultrasound Flyer</title>
<link href="https://fonts.googleapis.com/css2?family=Montserrat:wght@400;500;600;700;800&display=swap" rel="stylesheet">
<style>
  :root{
    --periwinkle:#7b86c4;
    --navy:#1f2b8f;
    --gold:#f7b417;
    --sand:#f1c85a;
    --paper:#f7f7f9;
    --ink:#3b3e52;
    --white:#ffffff;
    --backdrop:#e9e7e3;
  }
  *{box-sizing:border-box;margin:0;padding:0}
  html,body{width:1199px;height:1200px;overflow:hidden}
  body{background:var(--backdrop);font-family:"Montserrat",sans-serif;position:relative}

  .flyer{position:absolute;left:170px;top:15px;width:860px;height:1170px;background:var(--paper);overflow:hidden;box-shadow:0 4px 18px rgba(0,0,0,.12)}

  .hero-photo{position:absolute;left:380px;top:40px;width:480px;height:540px;
    background:linear-gradient(160deg,#e9ecf2 0%,#d9dce6 40%,#c9c4c2 70%,#eef0f4 100%)}

  .brand{position:absolute;right:36px;top:48px;display:flex;align-items:center;gap:12px}
  .brand-dot{width:18px;height:18px;border-radius:50%;background:var(--gold)}
  .brand-name{font-weight:800;font-size:50px;color:var(--navy);letter-spacing:2px;white-space:nowrap}

  .about-panel{position:absolute;left:0;top:68px;width:440px;height:835px;background:var(--periwinkle);border-top-right-radius:38px;padding:60px 30px 0 34px;color:var(--white)}
  .title{font-weight:700;font-size:48px;line-height:1.08;letter-spacing:1px;text-transform:uppercase}
  .title-rule{width:190px;height:3px;background:var(--gold);margin:22px 0 28px}
  .about-text{font-size:17px;line-height:1.5;text-align:justify;margin-bottom:22px;font-weight:500}
  .specialty-heading{color:var(--gold);font-weight:700;font-size:19px;line-height:1.3;margin:8px 0 18px}
  .specialties{list-style:none}
  .specialties li{display:flex;align-items:center;gap:20px;height:72px;font-size:20px;font-weight:500;letter-spacing:.5px;white-space:nowrap}
  .spec-icon{width:56px;height:56px;border-radius:50%;border:2px dotted var(--gold);background:rgba(255,255,255,.08);flex:none}

  .features-tab{position:absolute;left:500px;top:588px;width:360px;height:60px;background:var(--periwinkle);border-top-left-radius:22px;color:var(--white);font-weight:700;font-size:24px;display:flex;align-items:center;padding-left:40px;letter-spacing:.5px;white-space:nowrap}
  .features{position:absolute;right:36px;top:664px;width:370px;list-style:none;text-align:right;color:var(--ink)}
  .features li{position:relative;font-size:15px;line-height:1.3;padding-right:30px;margin-bottom:10px;font-weight:500}
  .features li svg{position:absolute;right:0;top:50%;transform:translateY(-50%)}

  .gallery{position:absolute;left:0;top:905px;width:860px;height:160px;display:flex;gap:12px;background:var(--paper)}
  .gallery div{flex:1}
  .shot-exam{background:linear-gradient(135deg,#e6eaef,#c9ccd6 60%,#f0eeec)}
  .shot-doppler{background:radial-gradient(circle at 50% 55%,#3a3a3a 0%,#111 55%,#050505 100%)}
  .shot-clinic{background:linear-gradient(135deg,#eef1f5,#bfc6d1 55%,#d7d3cf)}

  .footer-gold{position:absolute;left:0;top:1065px;width:860px;height:105px;background:var(--sand)}
  .footer-contact{position:absolute;left:0;top:1065px;width:480px;height:105px;background:var(--periwinkle);border-top-right-radius:52px;border-bottom-right-radius:52px;color:var(--white);padding:20px 0 0 30px;font-size:18px;font-weight:500}
  .footer-contact p{display:flex;align-items:center;gap:18px;height:32px;white-space:nowrap}
  .footer-web{position:absolute;right:30px;top:1084px;text-align:right;color:var(--white)}
  .footer-web small{display:block;font-size:15px;font-weight:500}
  .footer-web span{display:flex;align-items:center;gap:12px;font-size:22px;font-weight:600;letter-spacing:1.5px;white-space:nowrap}
</style>
</head>
<body>
<main class="flyer">
  <div class="hero-photo" role="img" aria-label="Sonographer scanning a patient's neck with an ultrasound probe"></div>

  <div class="brand">
    <span class="brand-dot"></span>
    <span class="brand-name">Vero M.Q.</span>
  </div>

  <section class="about-panel">
    <h1 class="title">Diagnostic<br>Ultrasound</h1>
    <div class="title-rule"></div>
    <p class="about-text">Vero M.Q. is a concierge ultrasound company that provides onsite or offsite diagnostic ultrasounds. We have over 14 years experience in sonography, business management, and customer service.</p>
    <p class="about-text">We offer both the physician and patient flexibility, convenience, and access to timely services.</p>
    <h2 class="specialty-heading">We provide ultrasounds for the following specialties:</h2>
    <ul class="specialties">
      <li><span class="spec-icon"></span>OBSTETRICS/GYNECOLOGY</li>
      <li><span class="spec-icon"></span>ABDOMINAL</li>
      <li><span class="spec-icon"></span>SMALL PARTS</li>
      <li><span class="spec-icon"></span>VASCULAR</li>
    </ul>
  </section>

  <div class="features-tab">COMPANY FEATURES:</div>
  <ul class="features">
    <li>Onsite or Offsite Scans<svg width="18" height="18" viewBox="0 0 18 18"><circle cx="9" cy="9" r="9" fill="var(--gold)"/><path d="M10.5 5 6.5 9l4 4" stroke="#fff" stroke-width="2" fill="none"/></svg></li>
    <li>Images Available Immediately for Referring<br>Physician and Patient<svg width="18" height="18" viewBox="0 0 18 18"><circle cx="9" cy="9" r="9" fill="var(--gold)"/><path d="M10.5 5 6.5 9l4 4" stroke="#fff" stroke-width="2" fill="none"/></svg></li>
    <li>Flexible Options for Ultrasound<br>Interpretation/Billing<svg width="18" height="18" viewBox="0 0 18 18"><circle cx="9" cy="9" r="9" fill="var(--gold)"/><path d="M10.5 5 6.5 9l4 4" stroke="#fff" stroke-width="2" fill="none"/></svg></li>
    <li>Access to Interpreting Radiologist<svg width="18" height="18" viewBox="0 0 18 18"><circle cx="9" cy="9" r="9" fill="var(--gold)"/><path d="M10.5 5 6.5 9l4 4" stroke="#fff" stroke-width="2" fill="none"/></svg></li>
    <li>Final Report Process -<br>1-2 Business Days/ 1 hour for STAT<svg width="18" height="18" viewBox="0 0 18 18"><circle cx="9" cy="9" r="9" fill="var(--gold)"/><path d="M10.5 5 6.5 9l4 4" stroke="#fff" stroke-width="2" fill="none"/></svg></li>
    <li>PACS Storage with Secure Access<svg width="18" height="18" viewBox="0 0 18 18"><circle cx="9" cy="9" r="9" fill="var(--gold)"/><path d="M10.5 5 6.5 9l4 4" stroke="#fff" stroke-width="2" fill="none"/></svg></li>
  </ul>

  <div class="gallery">
    <div class="shot-exam" role="img" aria-label="Pregnant patient receiving an obstetric ultrasound scan"></div>
    <div class="shot-doppler" role="img" aria-label="Colour Doppler ultrasound image on a dark screen"></div>
    <div class="shot-clinic" role="img" aria-label="Doctor performing an abdominal ultrasound on a male patient"></div>
  </div>

  <div class="footer-gold"></div>
  <div class="footer-contact">
    <p><svg width="20" height="20" viewBox="0 0 20 20"><circle cx="10" cy="10" r="10" fill="var(--gold)"/><path d="M7 5.5c-1 1-.6 3.4 1.6 5.7s4.7 2.8 5.7 1.7l.6-.9-2-1.5-1 .8c-.8-.3-2.2-1.7-2.6-2.6l.8-1-1.4-2z" fill="#fff"/></svg>+000 1234 5678</p>
    <p><svg width="20" height="20" viewBox="0 0 20 20"><circle cx="10" cy="10" r="10" fill="var(--gold)"/><path d="M10 4.5a3.5 3.5 0 0 0-3.5 3.5c0 2.6 3.5 7 3.5 7s3.5-4.4 3.5-7A3.5 3.5 0 0 0 10 4.5z" fill="#fff"/><circle cx="10" cy="8" r="1.3" fill="var(--gold)"/></svg>suscipit lobortis nisl ut aliquip ex ea com</p>
  </div>
  <div class="footer-web">
    <small>For more information</small>
    <span><svg width="22" height="22" viewBox="0 0 22 22" fill="none" stroke="#fff" stroke-width="1.6"><circle cx="11" cy="11" r="9"/><ellipse cx="11" cy="11" rx="4" ry="9"/><path d="M2 11h18M4 6h14M4 16h14"/></svg>www.yourwebsite.com</span>
  </div>
</main>
</body>
</html>
```